Loud Kite Promotional Banner

We are looking for a design for a 33.5" x 79" retractable pop-up banners to used at our live shows. We are a cover band that performs at clubs, corporate events, private parties, and weddings. We would have 2 banners, one on each side of the drum riser, and placed between the lighting trusses. Our website and Facebook page will provide information on what we are about - high energy fun entertainment of live music. We would like some marketing on the banner with logos, etc - something classy that can be used at almost any event. Contact information on the banners would be great. The banners do not have to be the exact same.

Website: www. loudkiteband.example
FB: https://www.social.example/Loudkitebandplano

I have uploaded a logo that can be used. Any other information, images, etc are available not the sites too.

Target Market(s)

New clients looking for a live band

Industry/Entity Type

Live Entertainment

Colors
0054AA
0677BA
7BADD7
CADEEF
E8F1F8
0094D4
00A9DD
6FCCEA
C7EBF8
E9F6FB

Requirements
Must have
• Logo, website address
Nice to have
• Images and excitement

```html
<!DOCTYPE html>
<html lang="en">
<head>
<meta charset="utf-8">
<title>Loud Kite Pop-up Banner</title>
<link rel="stylesheet" href="https://fonts.googleapis.com/css2?family=Bebas+Neue&family=Poppins:wght@400;500&display=swap">
<style>
  :root {
    --backdrop: #0e0e0e;
    --sky-top: #a9e1f1;
    --sky-mid: #6fc3e1;
    --sky-bottom: #1487b5;
    --white: #ffffff;
    --ink: #1c2a33;
    --shadow: rgba(0, 60, 90, 0.35);
    --photo-violet: #5a3fa8;
    --photo-plum: #6b4a78;
    --photo-navy: #1f2a5e;
    --photo-brick: #b9786a;
    --photo-stage: #3b2f52;
  }
  html, body {
    margin: 0;
    padding: 0;
    width: 821px;
    height: 1200px;
    overflow: hidden;
    background: var(--backdrop);
  }
  .banner {
    position: absolute;
    left: 206px;
    top: 117px;
    width: 409px;
    height: 965px;
    overflow: hidden;
    background: linear-gradient(180deg, var(--sky-top) 0%, var(--sky-mid) 50%, var(--sky-bottom) 100%);
    border-bottom: 5px solid var(--white);
    box-sizing: border-box;
  }
  .corner-shapes {
    position: absolute;
    left: 0;
    top: 0;
    width: 409px;
    height: 965px;
  }
  .photo {
    position: absolute;
    box-sizing: border-box;
    border: 2px solid var(--white);
    box-shadow: 1px 2px 4px var(--shadow);
  }
  .logo {
    position: absolute;
    left: 113px;
    top: 440px;
    width: 189px;
    height: 90px;
    display: flex;
    align-items: center;
    justify-content: center;
    gap: 12px;
  }
  .logo-mark {
    width: 22px;
    height: 22px;
    background: var(--white);
  }
  .logo-name {
    font-family: "Bebas Neue", sans-serif;
    font-size: 52px;
    line-height: 1;
    color: var(--white);
  }
  .headline {
    margin: 0;
    font-family: "Bebas Neue", sans-serif;
    font-weight: 400;
    color: var(--white);
  }
  .headline span {
    position: absolute;
    font-size: 74px;
    line-height: 1;
    white-space: nowrap;
  }
  .tagline {
    position: absolute;
    left: 0;
    width: 409px;
    top: 834px;
    margin: 0;
    text-align: center;
    font-family: "Poppins", sans-serif;
    font-size: 12.5px;
    line-height: 16.5px;
    color: var(--ink);
  }
  .website {
    position: absolute;
    left: 0;
    width: 409px;
    top: 922px;
    margin: 0;
    text-align: center;
    font-family: "Poppins", sans-serif;
    font-weight: 500;
    font-size: 17px;
    color: var(--white);
  }
</style>
</head>
<body>
  <main class="banner">
    <svg class="corner-shapes" viewBox="0 0 409 965" aria-hidden="true">
      <polygon points="0,20 66,86 0,152" fill="var(--shadow)"/>
      <polygon points="0,17 64,84 0,146" fill="var(--white)"/>
      <polygon points="409,420 345,484 409,548" fill="var(--shadow)"/>
      <polygon points="409,427 350,487 409,545" fill="var(--white)"/>
    </svg>

    <section class="gallery">
      <div class="photo" role="img" aria-label="Band performing in a ballroom" style="left:70px;top:131px;width:75px;height:58px;background:linear-gradient(160deg,#d8cde6,var(--photo-plum));"></div>
      <div class="photo" role="img" aria-label="Band on stage under a Friday night show sign" style="left:152px;top:106px;width:75px;height:83px;background:linear-gradient(160deg,#8a63d2,var(--photo-violet));"></div>
      <div class="photo" role="img" aria-label="Outdoor night concert crowd" style="left:234px;top:130px;width:134px;height:42px;background:linear-gradient(160deg,#3a4a8a,var(--photo-navy));"></div>
      <div class="photo" role="img" aria-label="Singer and guitarist under violet lights" style="left:22px;top:195px;width:89px;height:59px;background:linear-gradient(160deg,#7a5ad0,#2e2466);"></div>
      <div class="photo" role="img" aria-label="Full band on a lit stage" style="left:118px;top:195px;width:156px;height:97px;background:linear-gradient(160deg,#8a6a86,var(--photo-stage));"></div>
      <div class="photo" role="img" aria-label="Band members posing in front of a brick building" style="left:280px;top:177px;width:105px;height:123px;background:linear-gradient(180deg,#d9d2c8,var(--photo-brick) 45%,#2a2a2e);"></div>
      <div class="photo" role="img" aria-label="Band posing with wedding couple" style="left:35px;top:260px;width:76px;height:59px;background:linear-gradient(160deg,#b9a6e4,#3a3050);"></div>
      <div class="photo" role="img" aria-label="Vocalist dancing on stage" style="left:118px;top:299px;width:75px;height:89px;background:linear-gradient(160deg,#5a6fd0,#2a3480);"></div>
      <div class="photo" role="img" aria-label="Dance floor with guests and band" style="left:200px;top:299px;width:74px;height:59px;background:linear-gradient(160deg,#7ab050,#5a3a40);"></div>
      <div class="photo" role="img" aria-label="Bass player performing" style="left:280px;top:307px;width:75px;height:59px;background:linear-gradient(160deg,#3a5ab0,#1f2a4e);"></div>
    </section>

    <div class="logo">
      <span class="logo-mark"></span>
      <span class="logo-name">Loud Kite</span>
    </div>

    <h1 class="headline">
      <span style="left:79px;top:576px;">Parties,</span>
      <span style="left:112px;top:637px;">Weddings,</span>
      <span style="left:67px;top:693px;">&amp; Corporate</span>
      <span style="left:134px;top:753px;">Events</span>
    </h1>

    <p class="tagline">We love performing and providing<br>an incredible wedding celebrationexperience<br>for you and your guests!</p>

    <p class="website">www. loudkiteband.example</p>
  </main>
</body>
</html>
```